QBT Web Design Project

I would like a simple and elegant design for my international business consulting practice web site. I already have new QBT Logo and will have brochure-colors are blue, green and black

Practice areas:
I offer consulting services specializing in developing Internet-based anti-counterfeiting and anti-fraud programs, test purchases and investigations.

I offer Cyber Security, Data Protection and Compliance services

I also offer International Due Diligence Investigations and Country and Travel Risk Assessments

General Background Investigations

Physical Security Services

About me section listing my Bio

I have a set of key associates that I work with around the world and will want to list their CVs or Bios under "QBT

Associates"Banner with nice photo but not too cluttered

Ability to Upload documents and articles

Contact us section
Updates

I have uploaded my new logo-please advise if you didn't get it or it is not in the correct file format.

Thank you

Gordon

Hello Everyone,

Thank you for your submissions and ideas. I'm not sure about design only vs code. I understand that some of you do not do code-if not then please just provide design.

More about my business: see below link on Google docs to my brochure-this should help but don't use that phone number-see below.

https://files.example-docs.net/viewer?id=XK93PLQ7ZTR2MWN8&hl=en_US

 

Here are some details.

Contacts:

Gordon T. Vostrell, CPP

President

Vostrell and Partners, LLC

P.O. Box 47192

Gaithersburg, MD 20899

USA

web address:www.Vostrellandpartners.example (currently not working)

email:gord @vostrelland partners.example

Tel: 202-555-0147

I hope this is helpful. Gord

Reason: Sorry but during holiday period, have not had as much time to devote to this project. Thanks for your submissions.

Per my previous guidance, please keep designs simple and elegant and free from traditional security images with locks and chains-I prefer one or at most, two photos. Two colors- blue and green in addition to black for print. I want to present professional, corporate and international image. Thank you for your ideas nad submissions.

Gord

Target Market(s)

Law firms, large multi-national corporations, Security Industry

Industry/Entity Type

Business

Requirements
Must have
• Must have sections: (will provide text)

About QBT (will provide text)

Practice areas

Associates (will provide text)

Contact us

(it must also have ability to upload files and articles)
Should not have
• Old style fonts and symbols such as security badges, scales of justice, etc. I want a sleek and modern design.

```html
<!DOCTYPE html>
<html lang="en">
<head>
<meta charset="utf-8">
<title>QBT — Vostrell &amp; Partners, LLC</title>
<link rel="stylesheet" href="https://fonts.googleapis.com/css2?family=Noto+Sans:wght@400;500&family=Open+Sans:wght@400;600&display=swap">
<style>
:root{
  --blue:#0a5aa0;
  --blue-dark:#064f8f;
  --nav-top:#8fd2fb;
  --nav-bottom:#4fb4f2;
  --nav-line:#3c9bd8;
  --green:#6aab1c;
  --green-top:#a6dc5a;
  --green-bottom:#74bd2a;
  --text:#333;
  --grey-bg:#f1f1f1;
  --footer-bg:#d3d3d3;
  --frame:#6cc3f6;
  --white:#fff;
}
*{margin:0;padding:0;box-sizing:border-box}
html,body{width:1169px;height:1200px;overflow:hidden}
body{position:relative;background:var(--white);font-family:"Noto Sans",Verdana,sans-serif;color:var(--text)}
a{color:inherit;text-decoration:none}

/* header */
.brand{position:absolute;left:50px;top:38px}
.brand-row{display:flex;align-items:center;font-family:"Open Sans",sans-serif}
.brand-mark{font-size:35px;color:var(--blue);letter-spacing:-1px;padding-right:10px;border-right:1px solid #333;line-height:40px}
.brand-name{font-size:29px;color:#111;padding-left:10px;line-height:40px}
.brand-tag{font-size:17.5px;letter-spacing:2.6px;color:var(--blue);margin-top:6px;font-family:"Open Sans",sans-serif}
.search{position:absolute;left:883px;top:52px;width:199px;height:34px;border:3px solid #dfe9f3;background:var(--blue-dark);color:#fff;font-size:12px;line-height:28px;padding-left:10px}
.search-btn{position:absolute;left:1092px;top:54px}

/* nav */
.nav{position:absolute;left:46px;top:136px;width:1077px;height:61px;display:flex;background:linear-gradient(var(--nav-top),var(--nav-bottom));box-shadow:0 5px 6px -3px rgba(0,0,0,.35)}
.nav a{display:flex;align-items:center;justify-content:center;font-size:16px;color:#1b1b1b;border-right:1px solid var(--nav-line)}
.nav .active{background:linear-gradient(var(--green-top),var(--green-bottom))}
.nav .call{flex:1;border-right:0;gap:12px;font-size:17.5px}

/* slider */
.slider{position:absolute;left:114px;top:224px;width:942px;height:315px;background:var(--frame);border-radius:5px;box-shadow:0 14px 12px -10px rgba(0,0,0,.4)}
.slide-art{position:absolute;left:9px;top:9px;right:9px;bottom:12px;border-radius:3px;overflow:hidden;background:linear-gradient(180deg,#bcdcf8 0%,#e4f1fd 55%,#f4f9ff 100%)}
.slide-people{position:absolute;left:350px;top:100px;width:490px;bottom:0;background:linear-gradient(180deg,#3a3f47,#101216)}
.slide-copy{position:absolute;left:47px;top:58px;width:300px;z-index:1}
.slide-copy h2{font-weight:400;font-size:21px;color:var(--blue);white-space:nowrap;letter-spacing:.2px}
.slide-copy p{font-size:13.2px;line-height:22px;margin-top:10px;color:#333;width:290px}
.arrow{position:absolute;top:356px}
.arrow.prev{left:60px}.arrow.next{left:1071px}

/* welcome */
.welcome{position:absolute;left:80px;top:568px;width:1010px;text-align:center}
.welcome h1{font-weight:400;font-size:20.5px;color:var(--green)}
.welcome h1 span{color:var(--blue)}
.welcome p{font-size:14px;line-height:20px;margin-top:14px;padding:0 2px;letter-spacing:.3px}

/* services */
.services{position:absolute;left:0;top:698px;width:1169px;height:404px;background:var(--grey-bg);box-shadow:inset 0 10px 10px -10px rgba(0,0,0,.2)}
.services h2{position:absolute;left:49px;top:22px;font-weight:400;font-size:20.5px;color:var(--blue)}
.card{position:absolute;top:64px;width:261px;height:307px;background:#fff;border:1px solid #d6d6d6;border-radius:5px;box-shadow:0 2px 4px rgba(0,0,0,.18)}
.card h3{position:absolute;left:0;right:0;top:0;height:82px;display:flex;align-items:center;justify-content:center;text-align:center;font-weight:400;font-size:17.5px;line-height:25px;color:var(--green);padding:0 36px}
.card p{position:absolute;left:15px;right:16px;top:84px;font-size:12.6px;line-height:20px;text-align:justify}
.card .more{position:absolute;left:15px;bottom:17px;font-size:13.5px;color:var(--green);display:flex;align-items:center;gap:4px}
.card .icon{position:absolute;right:10px;bottom:8px;width:68px;height:56px;border-radius:4px;background:linear-gradient(135deg,#e8e8e8,#a9b3bd)}

/* footer */
.footer{position:absolute;left:0;top:1102px;width:1169px;height:98px;background:var(--footer-bg)}
.footer-links{position:absolute;top:18px;left:0;right:0;text-align:center;font-family:"Open Sans",sans-serif;font-size:12px;color:#222}
.footer-links span{margin:0 10px}
.copyright{position:absolute;left:48px;top:62px;font-family:"Open Sans",sans-serif;font-size:12px;color:#222}
.social{position:absolute;right:54px;top:54px;display:flex;align-items:center;gap:14px;font-family:"Open Sans",sans-serif;font-size:12px;color:#222}
.social i{display:block;width:25px;height:25px;border-radius:3px;background:var(--blue)}
</style>
</head>
<body>

<header>
  <div class="brand">
    <div class="brand-row"><span class="brand-mark">QBT</span><span class="brand-name">Vostrell &amp; Partners, LLC</span></div>
    <div class="brand-tag">Intellectual Property and Cyber Security</div>
  </div>
  <div class="search">Search...</div>
  <svg class="search-btn" width="26" height="28" viewBox="0 0 26 28" aria-label="Search">
    <circle cx="10" cy="10" r="7.5" fill="#cfe6fb" stroke="#2f7fc8" stroke-width="3"/>
    <line x1="15.5" y1="16" x2="23" y2="25" stroke="#2f7fc8" stroke-width="4.5" stroke-linecap="round"/>
  </svg>
</header>

<nav class="nav">
  <a class="active" href="#" style="width:125px">Home</a>
  <a href="#" style="width:155px">About QBT</a>
  <a href="#" style="width:181px">Practice Areas</a>
  <a href="#" style="width:154px">Associates</a>
  <a href="#" style="width:160px">Contact us</a>
  <a class="call" href="#">
    <svg width="24" height="24" viewBox="0 0 24 24" aria-hidden="true"><path d="M5 2c1-.6 2 0 2.6 1l2 3.6c.5 1 .2 1.9-.6 2.5l-1.4 1c.9 2.2 2.6 4 4.8 5l1-1.4c.6-.8 1.6-1.1 2.5-.6l3.6 2c1 .6 1.5 1.6 1 2.6-1 2.1-2.8 3.2-5 2.6C9.5 18.6 5.4 14.5 3.6 8.5 3 6.4 3.4 3.5 5 2z" fill="#111"/></svg>
    Call Us : 156 555 0193
  </a>
</nav>

<section class="slider">
  <div class="slide-art" role="img" aria-label="Banner photo: silhouettes of business people standing in a row against a light blue cloudy sky">
    <div class="slide-people"></div>
  </div>
  <div class="slide-copy">
    <h2>General Background Investigations</h2>
    <p>Curabitur blandit mauris eget libero euismod eu cursus mauris pretium Aliquam in orci a sapien tempor lacinia.</p>
  </div>
</section>
<svg class="arrow prev" width="34" height="50" viewBox="0 0 34 50" aria-label="Previous slide"><path d="M27 4 8 25l19 21" fill="none" stroke="#4aa9e8" stroke-width="8" stroke-linecap="round" stroke-linejoin="round"/></svg>
<svg class="arrow next" width="34" height="50" viewBox="0 0 34 50" aria-label="Next slide"><path d="M7 4l19 21L7 46" fill="none" stroke="#4aa9e8" stroke-width="8" stroke-linecap="round" stroke-linejoin="round"/></svg>

<section class="welcome">
  <h1>Welcome to <span>QBT</span></h1>
  <p>Many desktop publishing packages and web page editors now use Lorem Ipsum as their default model text, and a search for 'lorem ipsum' will uncover many web sites still in their infancy. Various versions have evolved over the years, sometimes by accident, sometimes on purpose (injected humour and the like).</p>
</section>

<section class="services">
  <h2>Our Services</h2>

  <article class="card" style="left:46px">
    <h3>Cyber Security</h3>
    <p>Many desktop publishing packages and web page editors now use Lorem Ipsum as their default model text, and many web sites still in their infancy. Various versions have evolved over the years, sometimes by accident, sometimes on purpose (injected humour and the like).</p>
    <a class="more" href="#">View more <svg width="12" height="10" viewBox="0 0 12 10"><path d="M1 1l4 4-4 4M6 1l4 4-4 4" fill="none" stroke="#6aab1c" stroke-width="2"/></svg></a>
    <div class="icon" role="img" aria-label="Illustration of a laptop"></div>
  </article>

  <article class="card" style="left:318px">
    <h3>General Background Investigations</h3>
    <p>Many desktop publishing packages and web page editors now use Lorem Ipsum as their default model text, and many web sites still in their infancy. Various versions have evolved over the years, sometimes by accident, sometimes on purpose (injected humour and the like).</p>
    <a class="more" href="#">View more <svg width="12" height="10" viewBox="0 0 12 10"><path d="M1 1l4 4-4 4M6 1l4 4-4 4" fill="none" stroke="#6aab1c" stroke-width="2"/></svg></a>
    <div class="icon" role="img" aria-label="Illustration of a row of figures under a magnifying glass" style="width:118px;height:40px;bottom:12px"></div>
  </article>

  <article class="card" style="left:591px">
    <h3>Data Protection</h3>
    <p>Many desktop publishing packages and web page editors now use Lorem Ipsum as their default model text, and many web sites still in their infancy. Various versions have evolved over the years, sometimes by accident, sometimes on purpose (injected humour and the like).</p>
    <a class="more" href="#">View more <svg width="12" height="10" viewBox="0 0 12 10"><path d="M1 1l4 4-4 4M6 1l4 4-4 4" fill="none" stroke="#6aab1c" stroke-width="2"/></svg></a>
    <div class="icon" role="img" aria-label="Illustration of a folder with a key" style="background:linear-gradient(135deg,#f3e3a8,#b99a3f)"></div>
  </article>

  <article class="card" style="left:864px">
    <h3>Physical Security Services</h3>
    <p>Many desktop publishing packages and web page editors now use Lorem Ipsum as their default model text, and many web sites still in their infancy. Various versions have evolved over the years, sometimes by accident, sometimes on purpose (injected humour and the like).</p>
    <a class="more" href="#">View more <svg width="12" height="10" viewBox="0 0 12 10"><path d="M1 1l4 4-4 4M6 1l4 4-4 4" fill="none" stroke="#6aab1c" stroke-width="2"/></svg></a>
    <div class="icon" role="img" aria-label="Illustration of a padlock with user figures" style="width:60px"></div>
  </article>
</section>

<footer class="footer">
  <div class="footer-links">
    <a href="#">Home</a><span>|</span><a href="#">About QBT</a><span>|</span><a href="#">Practice Areas</a><span>|</span><a href="#">Associates</a><span>|</span><a href="#">Contact us</a><span>|</span><a href="#">Sitemap</a>
  </div>
  <div class="copyright">Copyright © 2011 www.qbt.example &nbsp;&nbsp; All rights reserved</div>
  <div class="social">Connect with us :
    <i aria-label="Social network link"></i><i aria-label="Social network link"></i><i aria-label="Social network link"></i><i aria-label="Social network link"></i><i aria-label="Social network link"></i>
  </div>
</footer>

</body>
</html>
```